Enterprise Application UI beautification

We have an enterprise application that is being redesigned. A screenshot from the new UX/UI is provided. The current UI design is OK but we would like it to look better. The key goals of the UI are to look like a premium product (think luxury brand) and for it to be visually very appealing/attractive. When people see the UI we want them to have a significant, positive reaction. They should "ooh" and "ahh". This is a product sold to large enterprises, not consumers. The current UI is a little plain. The colors we want to use are blue, yellow, black, white and gray. We probably don't want different colors but feel free to use any variations within or close to that color scheme that you see fit. Also feel free to modify the spacing, icons, widgets, tables, fonts, etc.

Target Market(s)

Large enterprise customers (Summit 300).

Number of Pages Required

1 page

Font styles to use
Sans Serif

Colors
3277b5

Requirements
Must have
• A premium feel.

```html
<!DOCTYPE html>
<html lang="en">
<head>
<meta charset="utf-8">
<title>Data Sources · Skyledger Sandbox</title>
<link href="https://fonts.googleapis.com/css2?family=Mulish:wght@400;500;600;700;800&display=swap" rel="stylesheet">
<style>
:root{
  --navy-deep:#0e1c36;
  --navy:#16305c;
  --navy-mid:#1f4177;
  --blue:#3277b5;
  --blue-soft:#e4eef8;
  --gold:#f2b705;
  --gold-soft:#fff4cc;
  --gold-deep:#c9960a;
  --page:#eef0f4;
  --white:#ffffff;
  --tint:#f6f8fb;
  --ink:#111826;
  --text:#3b4352;
  --muted:#7c8594;
  --faint:#b7c0cc;
  --line:#e4e8ee;
}
*{box-sizing:border-box;margin:0;padding:0}
html,body{width:1200px;height:1018px;overflow:hidden}
body{font-family:'Mulish',sans-serif;background:var(--page);color:var(--text);position:relative;font-size:11px}

/* top bar */
.topbar{position:absolute;left:0;top:0;width:1200px;height:59px;background:var(--white);border-bottom:1px solid var(--line);box-shadow:0 2px 10px rgba(14,28,54,.05)}
.topbar:after{content:"";position:absolute;left:0;bottom:-1px;width:69px;height:2px;background:var(--gold)}
.brand{position:absolute;left:14px;top:19px;display:flex;align-items:center;gap:8px;font-weight:800;font-size:16px;color:var(--navy);letter-spacing:.4px}
.brand .dot{width:14px;height:14px;border-radius:50%;background:var(--gold)}
.user{position:absolute;right:36px;top:14px;display:flex;align-items:center;font-size:11px;color:var(--text)}
.avatar{width:30px;height:30px;border-radius:50%;background:radial-gradient(circle at 50% 40%,#b7a592,#3d4d66);box-shadow:0 0 0 2px var(--white),0 0 0 3px var(--gold);margin-right:12px}
.user .name{font-weight:700;color:var(--ink);font-size:10px;margin-right:28px}
.user .link{display:flex;align-items:center;gap:6px;margin-right:30px;font-size:11px;font-weight:600}
.user .link:last-child{margin-right:0}

/* icon rail */
.rail{position:absolute;left:0;top:59px;width:69px;height:959px;background:linear-gradient(180deg,var(--navy) 0%,var(--navy-deep) 100%)}
.rail-item{height:69px;border-bottom:1px solid rgba(255,255,255,.06);display:flex;align-items:center;justify-content:center;position:relative}
.rail-item.active{background:rgba(255,255,255,.07)}
.rail-item.active:before{content:"";position:absolute;left:0;top:0;width:3px;height:100%;background:var(--gold)}

/* source list */
.sources{position:absolute;left:69px;top:59px;width:253px;height:821px;background:var(--white);box-shadow:4px 0 18px rgba(14,28,54,.06)}
.sources h2{position:absolute;left:18px;top:28px;font-size:13.5px;font-weight:800;color:var(--navy);letter-spacing:.8px}
.sources h2:after{content:"";position:absolute;left:0;top:22px;width:26px;height:2px;background:var(--gold)}
.btn{display:inline-flex;align-items:center;gap:5px;border:1px solid #d9dee6;background:var(--white);border-radius:4px;font-size:11px;font-weight:600;color:var(--ink);padding:0 9px;height:21px}
.btn .plus{width:10px;height:10px;border-radius:50%;background:var(--gold);position:relative}
.btn .plus:before,.btn .plus:after{content:"";position:absolute;background:var(--navy-deep);left:2.5px;top:4.5px;width:5px;height:1px}
.btn .plus:after{left:4.5px;top:2.5px;width:1px;height:5px}
.sources .add{position:absolute;left:173px;top:25px;width:60px;justify-content:center}
.search{position:absolute;left:19px;top:61px;width:214px;height:31px;border:1px solid #dde2e9;border-radius:6px;background:var(--tint);display:flex;align-items:center;justify-content:space-between;padding:0 11px;font-size:11px;color:var(--muted)}
.list{position:absolute;left:0;top:118px;width:253px}
.src{padding:0 15px;display:flex;flex-direction:column;justify-content:center;border-bottom:1px solid var(--line);position:relative}
.src .t{font-size:12px;color:var(--ink);font-weight:500}
.src .s{font-size:9px;color:var(--muted);margin-top:2px}
.src.alt{background:var(--tint)}
.src.active{background:linear-gradient(90deg,var(--navy) 0%,var(--navy-mid) 100%);border-bottom:0}
.src.active:before{content:"";position:absolute;left:0;top:0;width:3px;height:100%;background:var(--gold)}
.src.active .t{color:#fff;font-weight:600}
.src.active .s{color:var(--gold)}
.src.active svg{position:absolute;right:16px;top:22px}

/* cards */
.card{position:absolute;left:350px;width:825px;background:var(--white);border-radius:8px;box-shadow:0 8px 28px rgba(14,28,54,.08),0 1px 3px rgba(14,28,54,.06)}
.card-info{top:94px;height:281px;border-top:3px solid var(--gold)}
.card-objects{top:400px;height:481px}
.card h1{position:absolute;left:19px;top:25px;font-size:19px;font-weight:800;color:var(--ink);letter-spacing:.2px}
.actions-row{position:absolute;left:284px;top:27px;display:flex;gap:10px}
.actions-row .btn{height:24px;gap:6px;padding:0 11px}
.actions-row .btn.primary{background:var(--navy);border-color:var(--navy);color:#fff}
.test{position:absolute;right:22px;top:27px;height:24px;padding:0 12px;border-radius:12px;background:var(--gold-soft);display:flex;align-items:center;gap:5px;font-size:11px;font-weight:700;color:var(--ink)}
.info{position:absolute;left:19px;top:72px;width:787px;border-collapse:collapse;font-size:10.5px;border-radius:6px;overflow:hidden}
.info td{height:36px;padding-left:27px;border-right:1px solid var(--line)}
.info td:last-child{border-right:0}
.info tr:nth-child(odd){background:var(--tint)}
.info td.k{color:var(--muted)}
.info td.v{color:var(--ink);font-weight:600}
.pill{display:inline-flex;align-items:center;gap:5px;padding:2px 9px;border-radius:10px;background:var(--gold-soft);color:var(--ink);font-weight:700}
.pill:before{content:"";width:6px;height:6px;border-radius:50%;background:var(--gold)}

.card-objects h1{top:21px}
.card-objects .add{position:absolute;left:184px;top:22px;width:60px;justify-content:center}
.obj-bar{position:absolute;left:19px;width:787px;height:39px;border-radius:6px;background:linear-gradient(90deg,var(--navy) 0%,var(--navy-mid) 100%);display:flex;align-items:center;color:#fff;font-size:16px;font-weight:600;letter-spacing:.2px}
.obj-bar.open{border-radius:6px 6px 0 0;box-shadow:inset 0 -2px 0 var(--gold)}
.toggle{width:25px;height:25px;border-radius:50%;background:rgba(255,255,255,.12);border:1px solid var(--gold);display:flex;align-items:center;justify-content:center;margin:0 8px 0 8px}
.obj-bar .x{margin-left:12px;font-size:12px;color:rgba(255,255,255,.6)}
.obj-bar .fields{position:absolute;right:13px;display:flex;align-items:center;gap:9px;font-size:10.5px;font-weight:700;letter-spacing:.6px;color:var(--gold)}
.obj-bar .fields .btn{border:0;height:20px;padding:0 12px;letter-spacing:0}

.fields-table{position:absolute;left:19px;top:102px;width:787px;border-collapse:collapse;font-size:10.5px;table-layout:fixed}
.fields-table th{background:var(--blue-soft);height:39px;text-align:left;font-weight:700;color:var(--navy);font-size:11px;white-space:nowrap}
.fields-table td{height:36px;border-right:1px solid var(--line);color:var(--ink)}
.fields-table td:last-child{border-right:0}
.fields-table tbody tr:nth-child(odd){background:var(--tint)}
.fields-table tbody tr:last-child td{border-bottom:1px solid var(--line)}
.c-name{width:142px;padding-left:27px}
th.c-name{padding-left:24px}
.c-type{width:175px;padding-left:22px}
th.c-type{padding-left:18px}
.c-pk{width:87px;padding-left:6px}
td.c-pk{padding-left:0;text-align:center}
.c-rule{width:158px;padding-left:30px}
th.c-rule{padding-left:30px}
.c-sens{width:125px;padding-left:26px}
th.c-sens{padding-left:17px}
.c-act{padding-left:27px}
th.c-act{padding-left:23px}
.chk{display:inline-block;width:10px;height:10px;border-radius:2px;background:#dbe3ed;vertical-align:middle}
.chk.on{background:var(--gold);position:relative}
.chk.on:after{content:"";position:absolute;left:3px;top:1px;width:3px;height:5px;border:solid var(--navy-deep);border-width:0 1.5px 1.5px 0;transform:rotate(45deg)}
.rules{display:flex;align-items:center;gap:7px}
.rules .a{font-size:15px;color:var(--ink);line-height:1;font-weight:600}
.icons{display:flex;align-items:center;gap:14px}

.footer-line{position:absolute;left:104px;top:939px;width:1061px;height:1px;background:#d6dbe3}
.copy{position:absolute;left:69px;width:1131px;top:973px;text-align:center;font-size:11px;color:var(--muted)}
.ver{position:absolute;right:17px;top:963px;font-size:8px;color:var(--muted)}
</style>
</head>
<body>
<header class="topbar">
  <div class="brand"><span class="dot"></span>Vantora</div>
  <div class="user">
    <div class="avatar" role="img" aria-label="User profile photo"></div>
    <span class="name">Alan Verso</span>
    <span class="link"><svg width="14" height="14" viewBox="0 0 14 14" fill="none" stroke="#3277b5" stroke-width="1.2"><circle cx="7" cy="7" r="2.2"/><circle cx="7" cy="7" r="5.5" stroke-dasharray="2 1.4"/></svg>Settings</span>
    <span class="link"><svg width="14" height="14" viewBox="0 0 14 14" fill="none" stroke="#3277b5" stroke-width="1.1"><rect x="1" y="2" width="12" height="10" rx="1"/><path d="M4 5l6 4M10 5l-6 4"/></svg>Logout</span>
  </div>
</header>

<nav class="rail">
  <div class="rail-item"><svg width="30" height="30" viewBox="0 0 30 30" fill="none" stroke="#fff" stroke-width="1.6"><circle cx="15" cy="6" r="3"/><circle cx="6" cy="9" r="2.5"/><circle cx="24" cy="9" r="2.5"/><path d="M10 27v-9a5 5 0 0110 0v9M3 24v-5a3 3 0 016 0M21 19a3 3 0 016 0v5M13 27v-5M17 27v-5"/></svg></div>
  <div class="rail-item"><svg width="30" height="22" viewBox="0 0 30 22" fill="none" stroke="#fff" stroke-width="1.6"><path d="M7 20a5 5 0 010-10 8 8 0 0115-2 6 6 0 012 12z"/></svg></div>
  <div class="rail-item active"><svg width="28" height="30" viewBox="0 0 28 30" fill="none" stroke="#f2b705" stroke-width="1.6"><rect x="3" y="2" width="18" height="20" rx="2"/><path d="M7 26h17V8M3 16h18"/></svg></div>
  <div class="rail-item"><svg width="28" height="32" viewBox="0 0 28 32" fill="none" stroke="#fff" stroke-width="1.6"><rect x="3" y="5" width="20" height="25" rx="2"/><rect x="9" y="2" width="8" height="5"/><path d="M7 13h12M7 18h10M7 23h6M15 25l3 3 7-8"/></svg></div>
  <div class="rail-item"><svg width="30" height="30" viewBox="0 0 30 30" fill="none" stroke="#fff" stroke-width="1.6"><rect x="2" y="5" width="24" height="22" rx="2"/><path d="M2 11h24M8 2v6M20 2v6M6 15h2M11 15h2M16 15h2M6 20h2M11 20h2"/><circle cx="22" cy="23" r="5" fill="#12264a"/><path d="M22 20v3h2"/></svg></div>
  <div class="rail-item"><svg width="30" height="30" viewBox="0 0 30 30" fill="none" stroke="#fff" stroke-width="1.6"><circle cx="7" cy="6" r="3"/><circle cx="23" cy="24" r="3"/><path d="M7 9v9a6 6 0 006 6h7M23 21v-9a6 6 0 00-6-6h-7M13 3l-3 3 3 3M17 27l3-3-3-3"/></svg></div>
</nav>

<aside class="sources">
  <h2>DATA SOURCES</h2>
  <span class="btn add"><span class="plus"></span>Add</span>
  <div class="search">Search<svg width="11" height="11" viewBox="0 0 11 11" fill="none" stroke="#7c8594" stroke-width="1.4"><circle cx="4.5" cy="4.5" r="3.5"/><path d="M7 7l3 3"/></svg></div>
  <div class="list">
    <div class="src active" style="height:58px"><span class="t">Skyledger - Sandbox</span><span class="s">Skyledger.net</span><svg width="14" height="14" viewBox="0 0 14 14" fill="none" stroke="#f2b705" stroke-width="1.6"><path d="M2 2l5 5-5 5M7 2l5 5-5 5"/></svg></div>
    <div class="src" style="height:55px"><span class="t">Stonebase Test 1 (administrator)</span><span class="s">StoneSQL</span></div>
    <div class="src alt" style="height:58px"><span class="t">Stonebase Test 2 (administrator)</span><span class="s">StoneSQL</span></div>
    <div class="src" style="height:55px"><span class="t">Sadga</span><span class="s">Skyledger.net</span></div>
    <div class="src alt" style="height:55px"><span class="t">Skyledger Test 1 (masterd ev)</span><span class="s">StoneSQL</span></div>
    <div class="src" style="height:57px"><span class="t">SKL - Field Entry Test</span><span class="s">Skyledger.net</span></div>
    <div class="src alt" style="height:55px"><span class="t">SKL 44</span><span class="s">Skyledger.net</span></div>
    <div class="src" style="height:54px"><span class="t">SKL 66</span><span class="s">Skyledger.net</span></div>
  </div>
</aside>

<section class="card card-info">
  <h1>Skyledger - Sandbox</h1>
  <div class="actions-row">
    <span class="btn primary"><svg width="10" height="10" viewBox="0 0 10 10"><path d="M1 9l1-3 5-5 2 2-5 5z" fill="#f2b705"/></svg>Edit</span>
    <span class="btn"><svg width="10" height="10" viewBox="0 0 10 10" fill="#16305c"><rect x="3" y="0" width="7" height="7"/><rect x="0" y="3" width="7" height="7" stroke="#fff"/></svg>Clone</span>
    <span class="btn"><svg width="9" height="9" viewBox="0 0 9 9" stroke="#16305c" stroke-width="1.8"><path d="M1 1l7 7M8 1l-7 7"/></svg>Delete</span>
  </div>
  <div class="test"><svg width="10" height="15" viewBox="0 0 12 18"><path d="M8 0L1 10h4l-2 8 8-11H7z" fill="#c9960a"/></svg>Test Connection</div>
  <table class="info">
    <tr><td class="k" style="width:173px">Data Source Name</td><td class="v" style="width:200px">Skyledger - Sandbox</td><td class="k" style="width:187px">Username</td><td class="v">masterdev@dev.northbase.net</td></tr>
    <tr><td class="k">Data Source Type</td><td class="v">Application</td><td class="k">Security Token</td><td class="v">tadkaji4234ifndkn3</td></tr>
    <tr><td class="k">Status</td><td class="v"><span class="pill">Active</span></td><td class="k">Environment Type</td><td class="v">Production</td></tr>
    <tr><td class="k">Created By</td><td class="v">harbor.test</td><td class="k">Connected App</td><td class="v">No</td></tr>
    <tr><td class="k">Last updated By</td><td class="v">harbor.test</td><td></td><td></td></tr>
  </table>
</section>

<section class="card card-objects">
  <h1>DATA OBJECTS</h1>
  <span class="btn add"><span class="plus"></span>Add</span>

  <div class="obj-bar open" style="top:64px">
    <span class="toggle"><svg width="12" height="8" viewBox="0 0 12 8" fill="none" stroke="#f2b705" stroke-width="2"><path d="M1 7l5-5 5 5"/></svg></span>Account<span class="x">✖</span>
    <span class="fields">FIELDS<span class="btn"><span class="plus"></span>Add</span></span>
  </div>

  <table class="fields-table">
    <thead><tr><th class="c-name">Field Name</th><th class="c-type">Data Type</th><th class="c-pk">Primary Key</th><th class="c-rule">Rule Types</th><th class="c-sens">Sensitive Data</th><th class="c-act">Actions</th></tr></thead>
    <tbody>
      <tr><td class="c-name">Account description</td><td class="c-type">Common.Text</td><td class="c-pk"><span class="chk on"></span></td><td class="c-rule"><span class="rules"><span class="a">a</span><svg width="60" height="12" viewBox="0 0 60 12" fill="none" stroke="#c3ccd8" stroke-width="1.3"><circle cx="5" cy="5" r="3.5"/><path d="M8 8l3 3"/><rect x="21" y="3" width="6" height="6" stroke="#111826"/><path d="M23 1h6v6" stroke="#111826"/><path d="M38 2v4h6V2M41 6v5"/><path d="M54 2l3 4-3 4-3-4z"/></svg><svg width="6" height="8" viewBox="0 0 6 8"><path d="M0 0l6 4-6 4z" fill="#d3dbe5"/></svg></span></td>
        <td class="c-sens"><span class="icons"><svg width="12" height="12" viewBox="0 0 12 12"><rect width="12" height="12" rx="2" fill="#16305c"/><path d="M3 6h6M6 3v6" stroke="#f2b705" stroke-width="1.6"/></svg><svg width="12" height="12" viewBox="0 0 12 12"><rect width="12" height="12" rx="2" fill="#16305c"/><path d="M3 6h6" stroke="#f2b705" stroke-width="1.6"/></svg><svg width="14" height="14" viewBox="0 0 14 14" fill="#16305c"><circle cx="7" cy="4" r="3.3"/><path d="M0 14a7 6 0 0114 0z"/></svg></span></td>
        <td class="c-act"><span class="icons"><svg width="14" height="14" viewBox="0 0 14 14"><path d="M1 13l1-4 8-8 3 3-8 8z" fill="#3277b5"/></svg><svg width="11" height="11" viewBox="0 0 11 11" stroke="#3277b5" stroke-width="2.2"><path d="M1 1l9 9M10 1l-9 9"/></svg></span></td></tr>
      <tr><td class="c-name">Account Fax</td><td class="c-type">Address. Address Line 3</td><td class="c-pk"><span class="chk"></span></td><td class="c-rule"><span class="rules"><span class="a">a</span><svg width="60" height="12" viewBox="0 0 60 12" fill="none" stroke="#c3ccd8" stroke-width="1.3"><circle cx="5" cy="5" r="3.5"/><path d="M8 8l3 3"/><rect x="21" y="3" width="6" height="6" stroke="#111826"/><path d="M23 1h6v6" stroke="#111826"/><path d="M38 2v4h6V2M41 6v5"/><path d="M54 2l3 4-3 4-3-4z"/></svg><svg width="6" height="8" viewBox="0 0 6 8"><path d="M0 0l6 4-6 4z" fill="#d3dbe5"/></svg></span></td><td class="c-sens"></td>
        <td class="c-act"><span class="icons"><svg width="14" height="14" viewBox="0 0 14 14"><path d="M1 13l1-4 8-8 3 3-8 8z" fill="#3277b5"/></svg><svg width="11" height="11" viewBox="0 0 11 11" stroke="#3277b5" stroke-width="2.2"><path d="M1 1l9 9M10 1l-9 9"/></svg></span></td></tr>
      <tr><td class="c-name">Account ID</td><td class="c-type">Common ID</td><td class="c-pk"><span class="chk"></span></td><td class="c-rule"><span class="rules"><span class="a">a</span><svg width="60" height="12" viewBox="0 0 60 12" fill="none" stroke="#c3ccd8" stroke-width="1.3"><circle cx="5" cy="5" r="3.5"/><path d="M8 8l3 3"/><rect x="21" y="3" width="6" height="6" stroke="#111826"/><path d="M23 1h6v6" stroke="#111826"/><path d="M38 2v4h6V2M41 6v5"/><path d="M54 2l3 4-3 4-3-4z"/></svg><svg width="6" height="8" viewBox="0 0 6 8"><path d="M0 0l6 4-6 4z" fill="#d3dbe5"/></svg></span></td><td class="c-sens"></td>
        <td class="c-act"><span class="icons"><svg width="14" height="14" viewBox="0 0 14 14"><path d="M1 13l1-4 8-8 3 3-8 8z" fill="#3277b5"/></svg><svg width="11" height="11" viewBox="0 0 11 11" stroke="#3277b5" stroke-width="2.2"><path d="M1 1l9 9M10 1l-9 9"/></svg></span></td></tr>
      <tr><td class="c-name">Account Name</td><td class="c-type">Address. Address Line 2</td><td class="c-pk"><span class="chk"></span></td><td class="c-rule"><span class="rules"><span class="a">a</span><svg width="60" height="12" viewBox="0 0 60 12" fill="none" stroke="#c3ccd8" stroke-width="1.3"><circle cx="5" cy="5" r="3.5"/><path d="M8 8l3 3"/><rect x="21" y="3" width="6" height="6" stroke="#111826"/><path d="M23 1h6v6" stroke="#111826"/><path d="M38 2v4h6V2M41 6v5"/><path d="M54 2l3 4-3 4-3-4z"/></svg><svg width="6" height="8" viewBox="0 0 6 8"><path d="M0 0l6 4-6 4z" fill="#d3dbe5"/></svg></span></td><td class="c-sens"></td>
        <td class="c-act"><span class="icons"><svg width="14" height="14" viewBox="0 0 14 14"><path d="M1 13l1-4 8-8 3 3-8 8z" fill="#3277b5"/></svg><svg width="11" height="11" viewBox="0 0 11 11" stroke="#3277b5" stroke-width="2.2"><path d="M1 1l9 9M10 1l-9 9"/></svg></span></td></tr>
    </tbody>
  </table>

  <div class="obj-bar" style="top:295px"><span class="toggle"><svg width="12" height="8" viewBox="0 0 12 8" fill="none" stroke="#f2b705" stroke-width="2"><path d="M1 1l5 5 5-5"/></svg></span>Asset<span class="x">✖</span></div>
  <div class="obj-bar" style="top:339px"><span class="toggle"><svg width="12" height="8" viewBox="0 0 12 8" fill="none" stroke="#f2b705" stroke-width="2"><path d="M1 1l5 5 5-5"/></svg></span>Asset Relationship<span class="x">✖</span></div>
  <div class="obj-bar" style="top:382px"><span class="toggle"><svg width="12" height="8" viewBox="0 0 12 8" fill="none" stroke="#f2b705" stroke-width="2"><path d="M1 1l5 5 5-5"/></svg></span>Asset Token Event<span class="x">✖</span></div>
  <div class="obj-bar" style="top:426px"><span class="toggle"><svg width="12" height="8" viewBox="0 0 12 8" fill="none" stroke="#f2b705" stroke-width="2"><path d="M1 1l5 5 5-5"/></svg></span>Case<span class="x">✖</span></div>
</section>

<div class="footer-line"></div>
<p class="copy">Copyright © company name. 2019. All rights reserved.</p>
<span class="ver">c7</span>
</body>
</html>
```